Driftline Harbor Sportfishing Tradeshow Booth

Im looking for a professional and attractive, eye catching trade show booth design

Target Market(s)

professionals who are looking to go on a high end fishing excursion

Industry/Entity Type

sport fishing

Requirements
Must have
• my website (www.driftlineharborsportfishing,com) my logo,

```html
<!DOCTYPE html>
<html lang="en">
<head>
<meta charset="utf-8">
<title>Driftline Harbor Sportfishing – Tradeshow Booth</title>
<link rel="stylesheet" href="https://fonts.googleapis.com/css2?family=Bebas+Neue&family=Poppins:ital,wght@0,600;0,700;1,700;1,800&display=swap">
<style>
  :root {
    --page: #ececee;
    --navy-deep: #072648;
    --navy: #0d3a6b;
    --ocean: #1f63a6;
    --band: #1f2a78;
    --white: #ffffff;
    --yellow: #fbe93a;
    --sky: #34a3f0;
    --logo-green: #7cc24a;
    --outline: #062038;
  }
  html, body {
    margin: 0;
    padding: 0;
    width: 701px;
    height: 1200px;
    overflow: hidden;
    background: var(--page);
  }
  .booth {
    position: absolute;
    left: 20px;
    top: 316px;
    width: 661px;
    height: 567px;
    overflow: hidden;
    box-shadow: 0 6px 18px rgba(0,0,0,.35);
    font-family: "Poppins", sans-serif;
  }
  .sea-backdrop {
    position: absolute;
    inset: 0;
    background:
      radial-gradient(ellipse 70% 30% at 60% 78%, rgba(70,140,210,.55), transparent 70%),
      linear-gradient(180deg, var(--navy-deep) 0%, var(--navy) 38%, #16508e 60%, var(--ocean) 80%, #2a6fb3 100%);
  }
  .brand-name {
    position: absolute;
    left: 60px;
    top: 80px;
    width: 190px;
    text-align: center;
    color: var(--logo-green);
    font-weight: 700;
    font-size: 27px;
    line-height: 1.15;
  }
  .headline {
    position: absolute;
    font-family: "Bebas Neue", sans-serif;
    transform: skewX(-9deg);
    line-height: 0.8;
    text-shadow: 2px 2px 0 var(--outline), -1px -1px 0 var(--outline), 1px -1px 0 var(--outline), -1px 1px 0 var(--outline);
    margin: 0;
  }
  .headline-tuna { left: 298px; top: 30px; font-size: 125px; color: var(--white); letter-spacing: 1px; }
  .headline-fishing { left: 282px; top: 131px; font-size: 104px; color: var(--yellow); letter-spacing: -1px; }
  .photo-strip { position: absolute; left: 0; top: 0; }
  .angler-cutout {
    position: absolute;
    left: 18px;
    top: 300px;
    width: 190px;
    height: 267px;
    border-radius: 40% 40% 0 0 / 22% 22% 0 0;
    background: linear-gradient(160deg, #5a4a3a 0%, #2b2a2c 40%, #6b2020 70%, #3a3030 100%);
  }
  .tagline {
    position: absolute;
    left: 227px;
    top: 411px;
    margin: 0;
    font-family: "Bebas Neue", sans-serif;
    font-size: 37px;
    color: var(--white);
    transform: skewX(-9deg);
    letter-spacing: -0.5px;
    white-space: nowrap;
  }
  .contact-band {
    position: absolute;
    left: 0;
    right: 0;
    top: 463px;
    bottom: 0;
    background: var(--band);
  }
  .contact-cutout-overlap {
    position: absolute;
    left: 18px;
    top: 463px;
    width: 190px;
    height: 104px;
    background: linear-gradient(180deg, #5a4636 0%, #3a2f2a 60%, #5c1c1c 100%);
  }
  .connect-label {
    position: absolute;
    left: 215px;
    top: 481px;
    color: var(--sky);
    font-weight: 800;
    font-style: italic;
    font-size: 13px;
    letter-spacing: 2px;
    margin: 0;
  }
  .phone-icon { position: absolute; left: 386px; top: 484px; }
  .phone-number {
    position: absolute;
    left: 420px;
    top: 473px;
    margin: 0;
    color: var(--white);
    font-weight: 800;
    font-style: italic;
    font-size: 27px;
    letter-spacing: 0.5px;
  }
  .website {
    position: absolute;
    left: 215px;
    top: 508px;
    margin: 0;
    color: var(--white);
    font-weight: 600;
    font-size: 15px;
  }
  .website .domain { color: var(--yellow); }
  .social-dots { position: absolute; left: 532px; top: 509px; display: flex; gap: 5px; }
  .social-dots span { width: 16px; height: 16px; border-radius: 50%; background: #4a67b8; }
</style>
</head>
<body>
  <main class="booth">
    <div class="sea-backdrop" role="img" aria-label="Deep blue ocean water with rolling waves"></div>

    <div class="brand-name">Driftline<br>Harbor</div>

    <h1 class="headline headline-tuna">TUNA</h1>
    <h1 class="headline headline-fishing">FISHING!</h1>

    <svg class="photo-strip" width="661" height="567" viewBox="0 0 661 567">
      <defs>
        <linearGradient id="catch-one" x1="0" y1="0" x2="0" y2="1">
          <stop offset="0" stop-color="#9fb2c4"/><stop offset="1" stop-color="#4c5560"/>
        </linearGradient>
        <linearGradient id="catch-two" x1="0" y1="0" x2="0" y2="1">
          <stop offset="0" stop-color="#a7b9c9"/><stop offset="0.5" stop-color="#7e8a97"/><stop offset="1" stop-color="#4a4f55"/>
        </linearGradient>
        <linearGradient id="catch-three" x1="0" y1="0" x2="0" y2="1">
          <stop offset="0" stop-color="#d9d6d2"/><stop offset="0.6" stop-color="#a9a6a6"/><stop offset="1" stop-color="#c9bcb8"/>
        </linearGradient>
      </defs>
      <g>
        <polygon points="65,227 242,227 221,377 53,377" fill="#fff"/>
        <polygon points="69,231 237,231 217,373 57,373" fill="url(#catch-one)" role="img" aria-label="Anglers on a boat holding a bluefin tuna"/>
      </g>
      <g>
        <polygon points="255,227 436,227 415,377 238,377" fill="#fff"/>
        <polygon points="259,231 431,231 411,373 243,373" fill="url(#catch-two)" role="img" aria-label="Four anglers on a dock holding flounder"/>
      </g>
      <g>
        <polygon points="452,227 632,227 610,377 433,377" fill="#fff"/>
        <polygon points="456,231 627,231 606,373 438,373" fill="url(#catch-three)" role="img" aria-label="A tuna landed on a boat deck"/>
      </g>
    </svg>

    <p class="tagline">GEAR UP WITH LOCAL EXPERTISE!</p>

    <div class="contact-band"></div>
    <div class="angler-cutout" role="img" aria-label="Angler holding a large tuna upright"></div>
    <div class="contact-cutout-overlap" role="img" aria-label="Lower part of angler holding a tuna"></div>

    <p class="connect-label">CONNECT WITH US</p>
    <svg class="phone-icon" width="24" height="24" viewBox="0 0 24 24" aria-hidden="true">
      <circle cx="12" cy="12" r="11" fill="#f6c31b"/>
      <path d="M8.2 6.5c.5-.4 1.1-.3 1.4.2l1.1 1.8c.3.5.2 1-.2 1.3l-.7.6c.6 1.4 1.6 2.5 3 3.2l.6-.7c.4-.4.9-.5 1.4-.2l1.8 1.1c.5.3.6.9.2 1.4l-.8 1c-.5.6-1.3.8-2 .5-3.1-1.2-5.4-3.6-6.5-6.6-.3-.7-.1-1.5.5-2z" fill="var(--band)"/>
    </svg>
    <p class="phone-number">555 014 2738</p>
    <p class="website">www.<span class="domain">driftlineharborsportfishing</span>.com</p>
    <div class="social-dots" aria-hidden="true"><span></span><span></span><span></span></div>
  </main>
</body>
</html>
```